Portal for Beautiful & Up-and-Coming Caribbean destination of KVT, Puerto Rico

We need the web design of an online portal for the KVT community of Puerto Rico. This should include the landing page, menu page, and at least one content page. The KVT area is a vibrant area in Northwest Puerto Rico with an airport, many local restaurants, beautiful beaches, and many things to do. I attach the logo which should be featured prominently, and we'll also be selling merchandise using this logo. The website should be a place for everyone in the community or tourists looking for things to do and places to stay. It will need to feature space and places for advertising as well. Also, we have a live hashtag feed (www.kvtvibe.example) where businesses and people in the community can hashtag their posts (we have licensed software that updates it every 30 minutes). We would like for the live hashtag feed to be part of the design, though the format can be changed a bit from what is currently in place. Indeed, the landing page should be changed to emphasize both the hashtag feed as well as the content of the site of KVTvibe. We need the landing page, menu page which will include 10-15 different modules or pages (examples: restaurants, things to do, places to stay, flights). I attach a spreadsheet which shows the menu pages that need to be featured. Comparable websites in our area are www.goshorevale.example and www.lagunapocket.example (but I don't like either one!). The final design should be contemporary, fresh, colorful fun and current, and communicate a vibrant and interactive community.

Target Market(s)

Tourists and people who live in this beach - oriented, beautiful community

Industry/Entity Type

Community

Number of Pages Required

3 page

Font styles to use
Sans Serif

Colors
33a6d7
f68e4e

Requirements
Must have
• landing page, menu design/page, and a sample content page. It must integrate a live hashtag feed, comparable to what is currently seen on www.kvtvibe.example. It must be fun, contemporary, colorful, unique, and clean. It must allow for advertising space.
Nice to have
• comments and interaction with visitors. Colors that integrate with the logo. Much emphasis on the logo, as we will also be selling merchandise.
Should not have
• extra squiggles and curlies and adornments.

```html
<!DOCTYPE html>
<html lang="en">
<head>
<meta charset="utf-8">
<title>KVT life — Community Portal</title>
<link href="https://fonts.googleapis.com/css2?family=Open+Sans:wght@400;600;700&family=PT+Sans+Narrow:wght@400;700&family=Alegreya+Sans:ital,wght@1,500&display=swap" rel="stylesheet">
<style>
:root{
  --blue:#33a6d7;
  --blue-dark:#1f8fc4;
  --orange:#f68e4e;
  --page:#ececec;
  --white:#ffffff;
  --ink:#3d3d3d;
  --text:#7a7a7a;
  --field:#ededed;
  --footer:#f3f3f3;
  --dark:#2b2b2b;
}
*{margin:0;padding:0;box-sizing:border-box}
html,body{width:1200px;height:3197px;overflow:hidden}
body{background:var(--page);font-family:"Open Sans",Arial,sans-serif;color:var(--ink);position:relative}
.site{position:absolute;left:17px;top:17px;width:1166px;height:3163px;background:var(--white)}
.abs{position:absolute}

/* header */
.brand{left:15px;top:26px;width:241px;height:159px;display:flex;align-items:center;justify-content:center;gap:10px}
.brand-dot{width:26px;height:26px;border-radius:50%;background:var(--blue)}
.brand-name{font-family:"PT Sans Narrow",sans-serif;font-weight:700;font-size:62px;color:var(--orange);letter-spacing:1px}
.social-top{left:776px;top:38px;display:flex;gap:6px}
.social-top span{width:27px;height:27px;border-radius:50%;background:var(--blue)}
.search{left:983px;top:38px;width:150px;height:28px;font-family:"PT Sans Narrow",sans-serif;font-size:13px;font-weight:700;color:#888;display:flex;align-items:center;justify-content:space-between}
.top-nav{right:28px;top:98px;display:flex;gap:14px;font-family:"PT Sans Narrow",sans-serif;font-weight:700;font-size:15px;color:var(--ink)}
.top-nav .active{color:var(--orange);border-top:2px solid var(--orange);padding-top:2px;margin-top:-4px}
.sub-nav{left:0;top:149px;width:1166px;height:36px;background:var(--blue);display:flex;justify-content:flex-end;align-items:center;gap:24px;padding-right:28px;font-family:"PT Sans Narrow",sans-serif;font-weight:700;font-size:14.5px;color:var(--white)}

/* hero */
.hero{left:0;top:185px;width:1166px;height:512px;background:linear-gradient(180deg,#b7a58e 0%,#c9b79e 35%,#a58d73 60%,#6fb2d6 85%,#3aa9dc 100%)}
.hero-caption{left:0;top:580px;width:1166px;text-align:center;font-family:"Open Sans",sans-serif;font-weight:700;font-size:29px;line-height:42px;color:var(--white)}

/* content cards */
.card{left:38px;width:702px;height:477px;background:var(--white);box-shadow:0 0 0 1px #e4e4e4}
.card-title{position:absolute;left:32px;top:36px;font-family:"PT Sans Narrow",sans-serif;font-weight:700;font-size:27px;color:var(--ink);text-transform:uppercase}
.card-photo{position:absolute;left:30px;top:83px;width:642px;height:198px}
.card-text{position:absolute;left:30px;top:298px;width:642px;font-size:14.6px;line-height:19.6px;color:var(--text)}
.btn{position:absolute;display:flex;align-items:center;justify-content:center;background:var(--orange);color:var(--white);font-family:"PT Sans Narrow",sans-serif;font-weight:700;font-size:15px}
.card .btn{left:512px;top:417px;width:160px;height:28px}
.divider{left:38px;width:702px;height:20px}
.divider::before{content:"";position:absolute;left:0;right:0;top:9px;border-top:2px dotted #bfdfee}
.divider span{position:absolute;left:340px;top:0;width:20px;height:20px;border-radius:50%;background:var(--blue);box-shadow:0 0 0 8px var(--white)}

/* sidebar */
.widget{left:789px;width:330px;background:var(--white);box-shadow:0 0 0 1px #e4e4e4}
.ribbon{left:761px;width:383px;height:38px}
.ribbon-label{position:absolute;left:0;top:0;width:383px;height:34px;display:flex;align-items:center;justify-content:center;font-family:"Alegreya Sans",sans-serif;font-style:italic;font-weight:500;font-size:20px;color:var(--white)}
.field{position:absolute;left:25px;width:277px;height:28px;background:var(--field);font-size:12.5px;color:#666;padding-left:14px;display:flex;align-items:center}
.posts{position:absolute;left:22px;top:70px;list-style:none}
.posts li{display:flex;gap:12px;font-size:14px;line-height:19px;color:var(--ink);margin-bottom:20px;width:280px}
.posts svg{flex:none;margin-top:2px}
.ad{left:789px;width:330px}
.ad-title{position:absolute;left:0;width:100%;text-align:center;font-family:"Open Sans",sans-serif;font-weight:700;color:var(--white);text-transform:uppercase}

/* gallery */
.gallery{left:43px;top:2406px;width:1080px;height:390px;display:grid;grid-template-columns:repeat(8,1fr);grid-template-rows:repeat(3,1fr)}

/* footer */
.footer{left:0;top:2828px;width:1166px;height:298px;background:linear-gradient(180deg,#f6f6f6,#e9eaea)}
.f-head{position:absolute;font-family:"PT Sans Narrow",sans-serif;font-weight:700;font-size:17px;color:var(--blue);text-transform:uppercase}
.f-links{position:absolute;list-style:none;font-family:"PT Sans Narrow",sans-serif;font-weight:700;font-size:14.5px;line-height:21px;color:var(--ink);text-transform:uppercase}
.f-copy{position:absolute;font-size:13.5px;line-height:19px;color:var(--ink)}
.f-input{position:absolute;left:433px;top:153px;width:225px;height:36px;background:var(--white);font-size:13px;color:#777;padding-left:14px;display:flex;align-items:center}
.f-btn{position:absolute;left:433px;top:203px;width:106px;height:36px;background:var(--dark);color:var(--white);font-family:"PT Sans Narrow",sans-serif;font-weight:700;font-size:14px;display:flex;align-items:center;justify-content:center}
.social-foot{position:absolute;left:703px;top:142px;display:flex;gap:9px}
.social-foot span{width:38px;height:38px;border-radius:50%;background:#4a4a4a}
.f-brand{position:absolute;left:960px;top:115px;font-family:"PT Sans Narrow",sans-serif;font-weight:700;font-size:52px;color:var(--orange)}
.copyright{left:0;top:3130px;width:1166px;height:30px;background:var(--orange);color:var(--white);font-size:10.5px;font-weight:600;display:flex;align-items:center;justify-content:center;text-transform:uppercase}
</style>
</head>
<body>
<div class="site">

  <header>
    <div class="abs brand"><span class="brand-dot"></span><span class="brand-name">KVT life</span></div>
    <div class="abs social-top" aria-label="Social links"><span></span><span></span><span></span><span></span><span></span></div>
    <div class="abs search">SEARCH SITE
      <svg width="16" height="16" viewBox="0 0 16 16"><circle cx="6.5" cy="6.5" r="5" fill="none" stroke="#999" stroke-width="2"/><line x1="10.5" y1="10.5" x2="15" y2="15" stroke="#999" stroke-width="2"/></svg>
    </div>
    <nav class="abs top-nav">
      <span class="active">HOME</span><span>EVENTS</span><span>COMMUNITY BLOG/REVIEWS</span><span>MAPS</span><span>GET INVOLVED</span><span>SURF &amp; WIND REPORTS</span><span>CONTACT</span>
    </nav>
    <nav class="abs sub-nav">
      <span>HISTORICAL SITES</span><span>SHOPPING</span><span>GETTING HERE &amp; AWAY</span><span>RESTAURANTS</span><span>LIVE ENTERTAINMENT</span><span>PLACES TO STAY</span><span>SCIENCE</span><span>REAL ESTATE</span>
    </nav>
  </header>

  <section class="abs hero" role="img" aria-label="Photo of two smiling travellers with a map pointing out sights on an old town street"></section>
  <p class="abs hero-caption">KVT area is a vibrant area in Northwest Puerto Rico with an airport,<br>many local restaurants, beautiful beaches, and many things to do.</p>

  <!-- articles -->
  <article class="abs card" style="top:757px">
    <h2 class="card-title">Historial Sites &amp; History of KVT</h2>
    <div class="card-photo" role="img" aria-label="Photo of a modern domed building by a lagoon at dusk" style="background:linear-gradient(180deg,#5b88b8 0%,#9fb6cf 45%,#3e4f66 70%,#1e2b3c 100%)"></div>
    <p class="card-text">Lorem ipsum dolor sit amet, consectetuer adipiscing elit, sed diam nonummy nibh euis mod tincidunt ut laoreet dolore magna aliquam erat volutpat. Ut wisi enim ad minim ve niam, quis nostrud exerci tation ullamcorper suscipit lobortis nisl ut aliquip ex ea comm odo consequat. Duis autem vel eum iriure dolor in hendrerit in vulputate velit esse mol estie consequat, vel illum dolore eu feugiat nulla.</p>
    <span class="btn">LEARN MORE</span>
  </article>
  <div class="abs divider" style="top:1262px"><span></span></div>

  <article class="abs card" style="top:1309px">
    <h2 class="card-title">Shopping Destinations in KVT</h2>
    <div class="card-photo" role="img" aria-label="Photo of three friends walking with shopping bags" style="background:linear-gradient(90deg,#c9b7a2 0%,#ece6df 35%,#e9e3dc 65%,#b7a79a 100%)"></div>
    <p class="card-text">Lorem ipsum dolor sit amet, consectetuer adipiscing elit, sed diam nonummy nibh euis mod tincidunt ut laoreet dolore magna aliquam erat volutpat. Ut wisi enim ad minim ve niam, quis nostrud exerci tation ullamcorper suscipit lobortis nisl ut aliquip ex ea comm odo consequat. Duis autem vel eum iriure dolor in hendrerit in vulputate velit esse mol estie consequat, vel illum dolore eu feugiat nulla.</p>
    <span class="btn">LEARN MORE</span>
  </article>
  <div class="abs divider" style="top:1810px"><span></span></div>

  <article class="abs card" style="top:1858px">
    <h2 class="card-title">Getting Here &amp; Away</h2>
    <div class="card-photo" role="img" aria-label="Photo of a coastal fortress on green lawns above the sea" style="background:linear-gradient(180deg,#7fa6c8 0%,#b9cbd9 35%,#6f8a5a 55%,#4f7a36 100%)"></div>
    <p class="card-text">Lorem ipsum dolor sit amet, consectetuer adipiscing elit, sed diam nonummy nibh euis mod tincidunt ut laoreet dolore magna aliquam erat volutpat. Ut wisi enim ad minim ve niam, quis nostrud exerci tation ullamcorper suscipit lobortis nisl ut aliquip ex ea comm odo consequat. Duis autem vel eum iriure dolor in hendrerit in vulputate velit esse mol estie consequat, vel illum dolore eu feugiat nulla.</p>
    <span class="btn">LEARN MORE</span>
  </article>
  <div class="abs divider" style="top:2360px;left:38px;width:1090px"><span style="left:535px"></span></div>

  <!-- sidebar -->
  <aside>
    <div class="abs widget" style="top:793px;height:266px">
      <div class="field" style="top:47px">Name</div>
      <div class="field" style="top:87px">Email Address</div>
      <div class="field" style="top:127px">Country</div>
      <div class="field" style="top:166px">Where are you visiting?</div>
      <span class="btn" style="left:64px;top:215px;width:201px;height:30px">GET TRAVEL TIPS</span>
    </div>
    <div class="abs ribbon" style="top:778px">
      <svg class="abs" width="383" height="38" viewBox="0 0 383 38"><polygon points="0,0 383,0 373,17 383,34 0,34 10,17" fill="var(--blue)"/><polygon points="28,34 28,38 18,34" fill="var(--blue-dark)"/><polygon points="355,34 355,38 365,34" fill="var(--blue-dark)"/></svg>
      <div class="ribbon-label">Discover the Beauty of KVT</div>
    </div>

    <div class="abs widget" style="top:1112px;height:256px">
      <ul class="posts">
        <li><svg width="16" height="16" viewBox="0 0 16 16"><circle cx="6.5" cy="6.5" r="5" fill="none" stroke="var(--blue)" stroke-width="2"/><line x1="10.5" y1="10.5" x2="15" y2="15" stroke="var(--blue)" stroke-width="2"/></svg><span>How to Escape and Discover the KVT</span></li>
        <li><svg width="16" height="16" viewBox="0 0 16 16"><circle cx="6.5" cy="6.5" r="5" fill="none" stroke="var(--blue)" stroke-width="2"/><line x1="10.5" y1="10.5" x2="15" y2="15" stroke="var(--blue)" stroke-width="2"/></svg><span>Discover the Untold Stories of KVT area</span></li>
        <li><svg width="16" height="16" viewBox="0 0 16 16"><circle cx="6.5" cy="6.5" r="5" fill="none" stroke="var(--blue)" stroke-width="2"/><line x1="10.5" y1="10.5" x2="15" y2="15" stroke="var(--blue)" stroke-width="2"/></svg><span>My 10 Favorite Things to do in KVT</span></li>
      </ul>
    </div>
    <div class="abs ribbon" style="top:1121px">
      <svg class="abs" width="383" height="38" viewBox="0 0 383 38"><polygon points="0,0 383,0 373,17 383,34 0,34 10,17" fill="var(--blue)"/><polygon points="28,34 28,38 18,34" fill="var(--blue-dark)"/><polygon points="355,34 355,38 365,34" fill="var(--blue-dark)"/></svg>
      <div class="ribbon-label">Recent Blog Posts</div>
    </div>

    <div class="abs ad" style="top:1398px;height:322px" role="img" aria-label="Advert photo of colourful fishing boats on a sunny beach" >
      <div class="abs" style="inset:0;background:linear-gradient(180deg,#4fb0dd 0%,#8fd0ec 45%,#d9cdb3 65%,#b44a3c 82%,#8a6e54 100%)"></div>
      <div class="ad-title" style="top:30px;width:190px;font-size:17px;line-height:21px">Surf<br>&amp; Wind<br>Reports</div>
      <span class="btn" style="left:27px;top:116px;width:158px;height:30px">LEARN MORE</span>
    </div>
    <div class="abs ad" style="top:1764px;height:243px" role="img" aria-label="Advert photo of friends gathered outdoors">
      <div class="abs" style="inset:0;background:linear-gradient(135deg,#3b8fb7 0%,#4aa6cf 50%,#2d7ea5 100%)"></div>
      <div class="ad-title" style="top:28px;width:190px;font-size:17px;line-height:21px">Find the Best<br>Accomodation<br>in the KVT</div>
      <span class="btn" style="left:27px;top:108px;width:158px;height:30px">LEARN MORE</span>
    </div>
    <div class="abs ad" style="top:2048px;height:286px" role="img" aria-label="Advert photo of a table laid with plates of local food">
      <div class="abs" style="inset:0;background:linear-gradient(135deg,#5a3a28 0%,#8a5a3a 45%,#6b4a35 70%,#3c2a20 100%)"></div>
      <div class="ad-title" style="top:78px;font-size:22px;line-height:26px">Restaurant<br>Ads</div>
      <span class="btn" style="left:66px;top:168px;width:196px;height:33px">LEARN MORE</span>
    </div>
  </aside>

  <!-- hashtag feed -->
  <section class="abs gallery" aria-label="Live hashtag feed">
    <div role="img" aria-label="Feed photo of green hills under clouds" style="grid-column:1/3;grid-row:1/3;background:linear-gradient(180deg,#8a97a4,#6a8a4a)"></div>
    <div role="img" aria-label="Feed photo of a sunset" style="background:linear-gradient(180deg,#3c3a3a,#8a5a3a)"></div>
    <div role="img" aria-label="Feed photo of people at a night event" style="background:#2c2a3c"></div>
    <div role="img" aria-label="Feed graphic about a three-day weekend" style="grid-column:5/7;grid-row:1/3;background:#f2c418"></div>
    <div role="img" aria-label="Feed photo of a grilled dish" style="background:#6a3a2a"></div>
    <div role="img" aria-label="Feed photo of a windmill by a street" style="background:linear-gradient(180deg,#8aa8c8,#6a8a5a)"></div>
    <div role="img" aria-label="Feed photo of an evening sky" style="background:linear-gradient(180deg,#5a6a8a,#c89060)"></div>
    <div role="img" aria-label="Feed photo of a night venue" style="background:#1e2436"></div>
    <div role="img" aria-label="Feed photo of guests at a bar" style="grid-column:7/9;background:#5a3a26"></div>
    <div role="img" aria-label="Feed photo of a lit archway" style="background:#d8a21e"></div>
    <div role="img" aria-label="Feed photo of a restaurant terrace" style="background:linear-gradient(180deg,#c8a070,#7a5a3a)"></div>
    <div role="img" aria-label="Feed photo of clouds at dusk" style="background:linear-gradient(180deg,#7a8aa0,#4a4a50)"></div>
    <div role="img" aria-label="Feed photo of a palm at night" style="background:#2a3a3a"></div>
    <div role="img" aria-label="Feed photo of an outdoor market" style="background:linear-gradient(180deg,#9ab0c0,#6a5a4a)"></div>
    <div role="img" aria-label="Feed photo of a plate of food" style="background:#b0483a"></div>
    <div role="img" aria-label="Feed photo of a person at a stall" style="grid-column:7/9;background:#3a2a22"></div>
  </section>

  <!-- footer -->
  <footer class="abs footer">
    <h3 class="f-head" style="left:38px;top:66px">Quick Links</h3>
    <ul class="f-links" style="left:38px;top:96px">
      <li>Events</li><li>Community Blog</li><li>Maps</li><li>Get Involved</li><li>Surf &amp; Wind Reports</li><li>Historical Sites</li><li>Shopping</li>
    </ul>
    <ul class="f-links" style="left:224px;top:96px">
      <li>Getting Here &amp; Away</li><li>Restaurants</li><li>Live Entertainment</li><li>Places to Stay</li><li>Science</li><li>Realestate</li><li>Contact</li>
    </ul>
    <h3 class="f-head" style="left:433px;top:66px">Newsletter Sign Up</h3>
    <p class="f-copy" style="left:433px;top:96px;width:240px">Stay informed about our news by signing up for our Newsletters.</p>
    <div class="f-input">Email</div>
    <div class="f-btn">SUBSCRIBE</div>
    <h3 class="f-head" style="left:703px;top:66px">Contact</h3>
    <p class="f-copy" style="left:703px;top:98px">info@kvtvibe.example</p>
    <h3 class="f-head" style="left:703px;top:112px;font-size:15px">Be Social With Us</h3>
    <div class="social-foot" aria-label="Social links"><span></span><span></span><span></span><span></span><span></span></div>
    <div class="f-brand">KVT life</div>
  </footer>
  <div class="abs copyright">Copyright © 2016 KVT life. All rights reserved.</div>

</div>
</body>
</html>
```